Menu Board 1000mmx500mm re-design

I would like to re-design exiting menu board 1000mmx500mm. Current board letters are bit to small to read. I would like to have pictures (attached) of the food offered on it and at the same time to create balance between pictures and size of the text to be easily readable. Fonts and colours are up to designer choice but prefer warm and bright colours rather anything dark.

Target Market(s)

Food industry

Industry/Entity Type

Food

Font styles to use
Other font styles liked:
• I leave font choice to designer

Colors
FFC000
F8CF3A
FAE287
FDF2CF
FEFAEE
F0912C
F2A743
F7CA91
FBE8D2
FDF5EE
EE7325
F08F49
F5BC92
FAE3D3
FDF4ED

Requirements
Must have
• Pictures + Text
Nice to have
• Balance between images and text.
Should not have
• Can't think of any

```html
<!DOCTYPE html>
<html lang="en">
<head>
<meta charset="UTF-8">
<title>Menu Board</title>
<link rel="stylesheet" href="https://fonts.googleapis.com/css2?family=Bebas+Neue&family=Poppins:wght@500;600&display=swap">
<style>
:root{
  --orange:#EE7325;
  --black:#0c0c0c;
  --white:#ffffff;
  --backdrop:#eeeeee;
  --gold-1:#FFC000;
  --gold-2:#F2A743;
  --gold-3:#F7CA91;
  --wood-1:#8a5a36;
  --wood-2:#5a3a22;
}
*{margin:0;padding:0;box-sizing:border-box}
html,body{width:699px;height:1200px;overflow:hidden;background:var(--backdrop)}
.board{position:absolute;left:97px;top:94px;width:506px;height:1012px;background:var(--white);overflow:hidden}
.title{position:absolute;left:0;width:100%;top:18px;text-align:center;font-family:"Bebas Neue",sans-serif;font-size:156px;line-height:1;letter-spacing:12px;color:var(--orange);padding-left:12px}
.hero{position:absolute;left:0;top:155px;width:100%;height:221px;background:radial-gradient(ellipse at 60% 40%,var(--gold-3),var(--gold-1) 45%,var(--gold-2) 80%,#b86a1f)}
.hero-rule{position:absolute;left:0;top:376px;width:100%;height:10px;background:var(--orange)}
.dish{position:absolute;width:151px;height:151px;border-radius:50%;border:2px solid var(--orange);background:var(--white);padding:5px}
.dish span{display:block;width:100%;height:100%;border-radius:50%}
.dish-1{left:25px;top:282px}
.dish-1 span{background:linear-gradient(160deg,#e8e4dc,#d9c7a0 45%,#a9779a 70%,#c9a06a)}
.dish-2{left:25px;top:439px}
.dish-2 span{background:radial-gradient(circle at 50% 50%,#f0b54a,#d98a2a 60%,#9a5a1e)}
.dish-3{left:25px;top:596px}
.dish-3 span{background:linear-gradient(180deg,#efe2c6,#e7c987 35%,#5f8c3a 55%,#e9cf95 80%,#f3efe8)}
.dish-4{left:25px;top:753px}
.dish-4 span{background:linear-gradient(170deg,#b9556a,#e7c0a8 40%,#7aa050 60%,#c7606d)}
.menu-panel{position:absolute;left:211px;top:439px;width:264px;height:461px;background:var(--black)}
.plate{position:absolute;left:200px;top:292px;width:284px;height:241px;border-radius:48% 52% 46% 54%/50% 48% 52% 50%;background:radial-gradient(ellipse at 55% 40%,#e8d3b0 0,#d8b27f 22%,var(--wood-1) 45%,var(--wood-2) 100%)}
.item{position:absolute;left:225px;width:240px;font-family:"Bebas Neue",sans-serif;color:var(--orange)}
.item-head{display:flex;justify-content:space-between;font-size:23px;line-height:19px}
.item-desc{font-family:"Poppins",sans-serif;font-weight:500;font-size:5.8px;line-height:7px;color:var(--white);margin-top:2px;max-width:180px}
.sauces{position:absolute;left:0;top:914px;width:100%;height:98px;background:var(--orange)}
.sauces-title{position:absolute;left:18px;top:4px;font-family:"Bebas Neue",sans-serif;font-size:90px;line-height:1;color:var(--black)}
.sauce-list{position:absolute;top:14px;list-style:none;font-family:"Poppins",sans-serif;font-weight:600;font-size:18px;line-height:24px;color:var(--white)}
.sauce-list-a{left:237px}
.sauce-list-b{left:409px}
</style>
</head>
<body>
<div class="board">
  <h1 class="title">MENU</h1>
  <div class="hero" role="img" aria-label="Golden roasted potatoes with thyme"></div>
  <div class="hero-rule"></div>

  <div class="dish dish-1"><span role="img" aria-label="Grilled chicken wrap with slaw"></span></div>
  <div class="dish dish-2"><span role="img" aria-label="Roasted potatoes with rosemary"></span></div>
  <div class="dish dish-3"><span role="img" aria-label="Grilled veggie wrap"></span></div>
  <div class="dish dish-4"><span role="img" aria-label="Beetroot wrap with chicken and salad"></span></div>

  <div class="menu-panel"></div>
  <div class="plate" role="img" aria-label="Roast chicken leg with veggie rice on a wooden plate"></div>

  <div class="item" style="top:563px"><div class="item-head"><span>Ciabatta</span><span>£6</span></div><p class="item-desc">Roti chicken, Rucola, Caramelized onion, &nbsp;Tomato, Fresh onions</p></div>
  <div class="item" style="top:603px"><div class="item-head"><span>Wrap</span><span>£7</span></div><p class="item-desc">Roti chicken, Crunchy slaw, Tomato, Fresh onion &amp; Sauce of your choice</p></div>
  <div class="item" style="top:650px"><div class="item-head"><span>Beetroot Wrap</span><span>£8</span></div><p class="item-desc">Roti chicken, Crunchy slaw, Tomato, Fresh onion &amp; Sauce of your choice</p></div>
  <div class="item" style="top:700px"><div class="item-head"><span>1/4 Chicken Box</span><span>£9</span></div><p class="item-desc">Roti chicken, Veggie rice &amp; Salad</p></div>
  <div class="item" style="top:743px"><div class="item-head"><span>1/2 Chicken Box</span><span>£14</span></div><p class="item-desc">Roti chicken, Veggie rice &amp; Salad</p></div>
  <div class="item" style="top:786px"><div class="item-head"><span>Roasted Potatoes</span><span>£2.5</span></div><p class="item-desc">Thyeme &amp; Garlic</p></div>
  <div class="item" style="top:827px"><div class="item-head"><span>Water</span><span>£1</span></div></div>
  <div class="item" style="top:864px"><div class="item-head"><span>Can &amp; Juices</span><span>£1.8</span></div></div>

  <div class="sauces">
    <h2 class="sauces-title">SAUCES</h2>
    <ul class="sauce-list sauce-list-a"><li>SIGNATURE</li><li>SWEET CHILLI</li><li>GARLIC MAYO</li></ul>
    <ul class="sauce-list sauce-list-b"><li>BBQ</li><li>PIRI PIRI</li></ul>
  </div>
</div>
</body>
</html>
```